Re-design of Business Card

We require a design for our business card.

Korrim is a supplier of industrial packaging specializing in plastic products. We are undergoing a rebranding to appear more corporate. We have changed our company name to korrim and have a new logo.

I have uploaded our old card design with the previous company name.
Don't copy the current design. We are looking for a new design.

Industry/Entity Type

Manufacturing

Contact Information for Business Card

please don't copy the current design. we are looking for a new design.

Font styles to use
Sans Serif

Colors

Designer to choose colors to be used in the design.

Requirements
Must have
• clean and easy to read.

```html
<!DOCTYPE html>
<html lang="en">
<head>
<meta charset="utf-8">
<title>Korrim Business Card</title>
<link rel="stylesheet" href="https://fonts.googleapis.com/css2?family=Arimo:wght@400;700&display=swap">
<style>
  :root {
    --orange-dark: #b5521c;
    --orange: #cf6d22;
    --orange-light: #dc8b32;
    --ink: #1d1d1d;
    --paper: #f4f5f8;
    --backdrop: #7f7f80;
  }
  * { margin: 0; padding: 0; box-sizing: border-box; }
  html, body { width: 1200px; height: 800px; overflow: hidden; }
  body {
    background: var(--backdrop);
    font-family: "Arimo", Arial, sans-serif;
    color: var(--ink);
    position: relative;
  }
  .card {
    position: absolute;
    top: 235px;
    width: 540px;
    height: 330px;
    background: var(--paper);
    overflow: hidden;
    box-shadow: 0 6px 18px rgba(0,0,0,.25);
  }
  .card--services { left: 40px; }
  .card--contact { left: 620px; }

  /* services side */
  .highlights {
    position: absolute; left: 0; top: 0; width: 100%; height: 78px;
    background: linear-gradient(90deg, var(--orange-dark), var(--orange) 45%, var(--orange-light));
  }
  .highlight {
    position: absolute; top: 0; height: 78px;
    display: flex; align-items: center; gap: 12px;
    color: #fff; font-weight: 700; font-size: 17px; line-height: 1.05;
  }
  .highlight::before {
    content: ""; width: 5px; height: 15px; background: #fff; flex: none;
  }
  .highlight--reach { left: 26px; }
  .highlight--haccp { left: 240px; }
  .highlight--iso { left: 452px; }

  .service { position: absolute; }
  .service__title {
    color: var(--orange); font-weight: 700; font-size: 18px; white-space: nowrap;
  }
  .service__items { list-style: none; font-size: 11.5px; line-height: 1.25; margin-top: 6px; }
  .service--left { left: 28px; }
  .service--left .service__items { padding-left: 20px; }
  .service--right { right: 28px; text-align: right; }
  .service::before {
    content: ""; position: absolute; top: 2px; width: 6px; height: 18px; background: var(--orange);
  }
  .service--left::before { left: -28px; }
  .service--right::before { right: -28px; }
  .service--containment { top: 98px; }
  .service--machinery { top: 228px; }
  .service--flexible { top: 90px; }
  .service--general { top: 186px; }

  /* contact side */
  .brand {
    position: absolute; left: 200px; top: 70px; width: 240px; text-align: center;
    color: var(--orange); font-weight: 700; font-size: 52px; letter-spacing: 1px;
  }
  .office, .person { position: absolute; font-size: 12px; line-height: 1.35; }
  .office { left: 28px; top: 182px; }
  .person { right: 28px; top: 206px; text-align: right; }
  .office::before, .person::before {
    content: ""; position: absolute; top: 0; width: 6px; height: 66px; background: var(--orange);
  }
  .office::before { left: -28px; }
  .person::before { right: -28px; }
  .block__title {
    color: var(--orange); font-weight: 700; font-size: 22px; line-height: 1.15; margin-bottom: 2px;
  }
  .address-band {
    position: absolute; left: 0; bottom: 0; width: 100%; height: 38px;
    background: linear-gradient(90deg, var(--orange-dark), var(--orange) 50%, var(--orange-light));
    color: #fff; font-size: 12.5px; display: flex; align-items: center; justify-content: center;
  }
</style>
</head>
<body>
  <section class="card card--services" aria-label="Card back: services">
    <div class="highlights">
      <div class="highlight highlight--reach"><span>Distribution<br>throughout<br>AUS &amp; NZ</span></div>
      <div class="highlight highlight--haccp"><span>HACCP<br>Certified</span></div>
      <div class="highlight highlight--iso"><span>ISO<br>9001</span></div>
    </div>

    <div class="service service--left service--containment">
      <h2 class="service__title">Pallet Containment</h2>
      <ul class="service__items"><li>Stretch</li><li>Heat Shrink</li><li>Pallet Hood</li></ul>
    </div>
    <div class="service service--left service--machinery">
      <h2 class="service__title">Pallet Wrapping Machinery</h2>
      <ul class="service__items"><li>Semi &amp; Fully auto Lines</li><li>Finance options include Lease, rent or pay per warp</li></ul>
    </div>
    <div class="service service--right service--flexible">
      <h2 class="service__title">Flexible Packaging</h2>
      <ul class="service__items"><li>Bags &amp; Liners</li><li>Tube</li><li>Film &amp; Sheet</li><li>Printed Films (12 col)</li><li>Shrink films</li></ul>
    </div>
    <div class="service service--right service--general">
      <h2 class="service__title">General Packgaging</h2>
      <ul class="service__items"><li>Bags &amp; Liners</li><li>Tube</li><li>Film &amp; Sheet</li><li>Printed Films (12 col)</li><li>Shrink films</li></ul>
    </div>
  </section>

  <section class="card card--contact" aria-label="Card front: contact">
    <div class="brand">KORRIM</div>
    <div class="office">
      <h2 class="block__title">Head Office</h2>
      <p>1300 555 014</p>
      <p>+61 7 5550 1234</p>
      <p>www.korrim.com.au</p>
    </div>
    <div class="person">
      <h2 class="block__title">Declan Hart</h2>
      <p>Machinery Sales Manager</p>
      <p>xxxx xxx xx</p>
      <p>declanh@korrim.com.au</p>
    </div>
    <div class="address-band">48 Harlow St Eastbrook, Qld 4120 Australia</div>
  </section>
</body>
</html>
```